New menu rebranding for Asian fusion

I have my current menu attached, but I want to change it and make it more attractive. The restaurant is an Asian Fusion. Food from Thailand, China, Japan, Indonesia, Malaysia, Cambodia. We cater to mid to high end consumers with an educated and sophisticated pallet. Maybe try a modern twist, or an authentic variation, maybe a mix. Please don't play with the logo too much, but feel free to play with the pattern. I also want to have as many pictures of dishes visible as possible. Additionally, keep in mind that the menu will be in two languages, so please design accordingly. Feel free to play around with the format of the menu and the logo too if you get carried away. Keep it in mind that this is also a take out menu too. Please check out the Instagram account lotus_crate As well as facebook etc. Let me know if you need any additional files. Thx and appreciated.
Updates

I have made an update to the Menu. It's not the original file. It's smaller now. Please see the attached PDF file. Best regards, Added Monday, February 02, 2015

Project Deadline Extended
Reason: Because I posted an update image to the new revised menu.

Target Market(s)

Mid to high end

Industry/Entity Type

Restaurant

Number of Pages Required

3 page

Requirements
Must have
• dual language friendly. At least make space for it.
• Must keep logo.
Nice to have
• Would be nice to stick to same theme, not too much change to branding.

```html
<!DOCTYPE html>
<html lang="en">
<head>
<meta charset="utf-8">
<title>Appetizers Menu</title>
<link rel="stylesheet" href="https://fonts.googleapis.com/css2?family=Oswald:wght@300;400;500&family=Harmattan:wght@400;700&display=swap">
<style>
  :root {
    --ink: #000000;
    --stripe: #1c1c1c;
    --orange: #f7941d;
    --white: #ffffff;
    --frame: #f4f4f4;
  }
  * { margin: 0; padding: 0; box-sizing: border-box; }
  html, body { width: 1200px; height: 849px; overflow: hidden; background: var(--ink); }
  .menu-page {
    position: relative; width: 1200px; height: 849px; overflow: hidden;
    background: repeating-linear-gradient(90deg, var(--ink) 0 40px, var(--stripe) 40px 80px);
    font-family: "Oswald", sans-serif;
  }
  .menu-panel {
    position: absolute; left: 62px; top: 62px; width: 1078px; height: 706px;
    background: var(--ink);
  }
  .page-title {
    position: absolute; left: 92px; top: 82px;
    color: var(--orange); font-weight: 300; font-size: 60px; letter-spacing: -1px;
    white-space: nowrap;
  }
  .page-title .ar { font-family: "Harmattan", sans-serif; font-weight: 400; font-size: 58px; }
  .dish { position: absolute; width: 440px; }
  .dish-number {
    position: absolute; left: 0; top: 0; width: 54px; height: 38px;
    background: var(--orange); color: var(--ink);
    font-weight: 500; font-size: 24px; line-height: 38px; text-align: center;
  }
  .dish-name {
    position: absolute; left: 66px; top: 0; color: var(--orange);
    font-weight: 400; font-size: 23px; line-height: 38px; white-space: nowrap; letter-spacing: -0.3px;
  }
  .dish-name .ar { font-family: "Harmattan", sans-serif; font-size: 22px; }
  .dish-price {
    position: absolute; left: 408px; top: 0; color: var(--orange);
    font-weight: 400; font-size: 23px; line-height: 38px;
  }
  .dish-desc {
    position: absolute; left: 65px; top: 48px; width: 430px; color: var(--white);
    font-weight: 300; font-size: 19.5px; line-height: 27px; letter-spacing: -0.2px;
  }
  .dish-desc-ar {
    position: absolute; left: 65px; top: 101px; width: 425px; color: var(--white);
    font-family: "Harmattan", sans-serif; font-weight: 700; font-size: 18px; line-height: 27px;
    direction: rtl; text-align: left;
  }
  .dish-photo {
    position: absolute; border: 5px solid var(--frame);
    box-shadow: 0 2px 8px rgba(0,0,0,0.5);
  }
  .photo-tag {
    position: absolute; bottom: 4px; left: 8px; padding: 0 6px;
    background: var(--ink); color: var(--white);
    font-weight: 500; font-size: 18px; line-height: 26px;
  }
</style>
</head>
<body>
<main class="menu-page">
  <div class="menu-panel"></div>

  <h1 class="page-title">Appetizers / <span class="ar">مقبلات</span></h1>

  <div class="dish-photo" style="left:580px;top:40px;width:210px;height:142px;transform:rotate(-3deg);background:linear-gradient(135deg,#d8c9a0,#7a4a22 55%,#5d7a2c);" role="img" aria-label="Chicken satay skewers with peanut sauce and lime"><span class="photo-tag">101</span></div>
  <div class="dish-photo" style="left:778px;top:35px;width:230px;height:152px;background:linear-gradient(135deg,#e8a040,#c8561c 50%,#8a4a20);" role="img" aria-label="Grilled shrimp satay with dipping sauce"><span class="photo-tag">102</span></div>
  <div class="dish-photo" style="left:1003px;top:30px;width:168px;height:172px;transform:rotate(2deg);background:linear-gradient(135deg,#c05a3a,#5a1a14 60%,#e8e0dc);" role="img" aria-label="Crispy spiced dendeng beef"><span class="photo-tag">103</span></div>
  <div class="dish-photo" style="left:618px;top:602px;width:236px;height:174px;transform:rotate(-2deg);background:linear-gradient(135deg,#e6d3ae,#cfb485 55%,#c82a1e);" role="img" aria-label="Fried calamari with sweet chili sauce"><span class="photo-tag">104</span></div>
  <div class="dish-photo" style="left:858px;top:604px;width:240px;height:162px;background:linear-gradient(135deg,#4e8a34,#d8963e 50%,#b8541c);" role="img" aria-label="Crispy spring rolls with fresh greens"><span class="photo-tag">105</span></div>

  <section class="dish" style="left:92px;top:216px;">
    <div class="dish-number">101</div>
    <h2 class="dish-name">Chicken Satay / <span class="ar">ساتيه الدجاج</span></h2>
    <div class="dish-price">SR25</div>
    <p class="dish-desc">Lorem ipsum dolor sit amet, consectetuer adipiscing elit, sed diam nonummy nibh euismod tincidunt ut laoreet.</p>
    <p class="dish-desc-ar">أسياخ الدجاج شريط BQ منقع في الأعشاب التايلاندية تقدم مع صلصة الفول السوداني منعش الحلو</p>
  </section>

  <section class="dish" style="left:92px;top:386px;">
    <div class="dish-number">102</div>
    <h2 class="dish-name">Shrimp Satay / <span class="ar">ساتيه الدجاج</span></h2>
    <div class="dish-price">SR30</div>
    <p class="dish-desc">Lorem ipsum dolor sit amet, consectetuer adipiscing elit, sed diam nonummy nibh euismod tincidunt ut laoreet.</p>
    <p class="dish-desc-ar">شريط BQ أسياخ الروبيان المتبل في الأعشاب التايلاندية تقدم مع صلصة الفول السوداني منعش</p>
  </section>

  <section class="dish" style="left:92px;top:562px;">
    <div class="dish-number">103</div>
    <h2 class="dish-name">Dendeng / <span class="ar">دن دينغ</span></h2>
    <div class="dish-price">SR38</div>
    <p class="dish-desc">Lorem ipsum dolor sit amet, consectetuer adipiscing elit, sed diam nonummy nibh euismod tincidunt ut laoreet.</p>
    <p class="dish-desc-ar">شريط BQ أسياخ الروبيان المتبل في الأعشاب التايلاندية تقدم مع صلصة الفول السوداني منعش</p>
  </section>

  <section class="dish" style="left:605px;top:216px;">
    <div class="dish-number">104</div>
    <h2 class="dish-name">Calamari / <span class="ar">ساتيه الدجاج</span></h2>
    <div class="dish-price">SR28</div>
    <p class="dish-desc">Lorem ipsum dolor sit amet, consectetuer adipiscing elit, sed diam nonummy nibh euismod tincidunt ut laoreet.</p>
    <p class="dish-desc-ar">أسياخ الدجاج شريط BQ منقع في الأعشاب التايلاندية تقدم مع صلصة الفول السوداني منعش الحلو</p>
  </section>

  <section class="dish" style="left:605px;top:386px;">
    <div class="dish-number">105</div>
    <h2 class="dish-name">Spring Rolls / <span class="ar">ساتيه الدجاج</span></h2>
    <div class="dish-price">SR23</div>
    <p class="dish-desc">Lorem ipsum dolor sit amet, consectetuer adipiscing elit, sed diam nonummy nibh euismod tincidunt ut laoreet.</p>
    <p class="dish-desc-ar">شريط BQ أسياخ الروبيان المتبل في الأعشاب التايلاندية تقدم مع صلصة الفول السوداني منعش</p>
  </section>
</main>
</body>
</html>
```